Zielgruppe
Unter dem Markennamen Kestrilo vertreiben wir Produkte, welche von uns selbst entwickelt werden. Ein Bestandteil eines jeden Produktes ist dabei immer etwas aus Bambus. Die Zielgruppe ist sehr unspezifisch, aber eher junge Erwachsene und Erwachsene im mittleren Alter. Bei den Produkten handelt es sich um Haushaltsprodukte bzw. kleinere Möbelstücke. Für ein neues Schneidebrett Set wird jetzt ein schönes Verpackungsdesign gesucht.
Aufgabenstellung
Wir haben ein komplettes Briefing mit unseren Vorstellungen erstellt.

```html
<!DOCTYPE html>
<html lang="de">
<head>
<meta charset="utf-8">
<title>Kestrilo – Schneidebrett Set Bambus – Verpackung</title>
<link rel="stylesheet" href="https://fonts.googleapis.com/css2?family=Josefin+Sans:wght@300&family=Oswald:wght@600&family=Montserrat:wght@400;700&display=swap">
<style>
  :root {
    --bg: #c6bfb4;
    --box: #f7f7f5;
    --ink: #1c1c1c;
    --green: #4a7a2c;
    --wood: #c99a5b;
    --fold: #dcdcd8;
    --icon: #e6e6e2;
  }
  * { box-sizing: border-box; margin: 0; padding: 0; }
  html, body { width: 1200px; height: 833px; overflow: hidden; background: var(--bg); }
  .canvas { position: relative; width: 1200px; height: 833px; }

  .panel { position: absolute; background: var(--box); }
  .lid { left: 50px; top: 30px; width: 960px; height: 470px; }
  .front { left: 50px; top: 500px; width: 960px; height: 290px; border-top: 2px solid var(--fold); }
  .end { left: 1010px; top: 500px; width: 140px; height: 290px; border-top: 2px solid var(--fold); border-left: 2px solid var(--fold); }

  .wordmark {
    font-family: "Josefin Sans", sans-serif;
    font-weight: 300;
    color: var(--ink);
    letter-spacing: 4px;
  }
  .label {
    font-family: "Oswald", sans-serif;
    font-weight: 600;
    color: var(--ink);
    text-transform: uppercase;
  }

  /* lid */
  .lid .wordmark { position: absolute; left: 120px; top: 40px; font-size: 64px; line-height: 1; }
  .lid .product-title { position: absolute; left: 128px; top: 116px; font-size: 19px; letter-spacing: .3px; }
  .bamboo-photo {
    position: absolute; left: 40px; top: 170px; width: 220px; height: 280px;
    background: radial-gradient(ellipse at 55% 50%, #a6d35a 0%, #d9ecc0 45%, var(--box) 72%);
  }
  .set-info { position: absolute; left: 310px; top: 235px; width: 120px; text-align: center; }
  .set-info .label { font-size: 17px; display: block; margin-bottom: 12px; }
  .use-icons { list-style: none; display: flex; flex-direction: column; align-items: center; gap: 10px; }
  .use-icon { width: 44px; height: 34px; border: 2px solid var(--ink); border-radius: 50%; background: var(--icon); }
  .green-band { position: absolute; left: 540px; top: 0; width: 14px; height: 470px; background: var(--green); }
  .kitchen-photo {
    position: absolute; left: 554px; top: 0; width: 406px; height: 370px;
    background: linear-gradient(160deg, #e9e3d9 0%, #b98e55 45%, #c99a5b 65%, #7d3a63 85%, #e8e2d8 100%);
  }
  .features {
    position: absolute; left: 575px; top: 385px;
    font-family: "Montserrat", sans-serif; font-size: 12px; line-height: 1.35; color: var(--ink);
  }
  .features strong { font-weight: 700; display: block; }
  .care { position: absolute; left: 780px; top: 380px; width: 170px; text-align: center; }
  .care svg { display: block; margin: 0 auto 6px; }
  .care span { font-family: "Montserrat", sans-serif; font-size: 9px; color: var(--ink); letter-spacing: .2px; }

  /* front */
  .front .wordmark { position: absolute; left: 70px; top: 70px; font-size: 54px; line-height: 1; }
  .front .product-title { position: absolute; left: 78px; top: 138px; font-size: 14px; letter-spacing: .3px; }
  .product-shots { position: absolute; left: 440px; top: 60px; display: flex; gap: 40px; }
  .product-shot {
    width: 135px; height: 135px; border-radius: 4px;
    background: linear-gradient(135deg, #e2c08d, var(--wood) 55%, #a97b40);
  }

  /* end */
  .imprint {
    position: absolute; left: 20px; top: 30px; width: 100px; height: 230px;
    display: flex; align-items: center; justify-content: center;
  }
  .imprint p {
    transform: rotate(-90deg); white-space: nowrap;
    font-family: "Montserrat", sans-serif; font-size: 9px; line-height: 1.5; color: var(--ink); text-align: center;
  }
</style>
</head>
<body>
<main class="canvas">
  <section class="panel lid">
    <h1 class="wordmark">KESTRILO</h1>
    <p class="label product-title">Schneidebrett Set Bambus</p>
    <div class="bamboo-photo" role="img" aria-label="Foto: grüne Bambuszweige mit Blättern"></div>
    <div class="set-info">
      <span class="label">4er-Set</span>
      <ul class="use-icons">
        <li class="use-icon" role="img" aria-label="Liniensymbol Gemüse"></li>
        <li class="use-icon" role="img" aria-label="Liniensymbol Brot"></li>
        <li class="use-icon" role="img" aria-label="Liniensymbol Fleisch"></li>
        <li class="use-icon" role="img" aria-label="Liniensymbol Fisch"></li>
      </ul>
    </div>
    <div class="green-band"></div>
    <div class="kitchen-photo" role="img" aria-label="Foto: Hände schneiden Rotkohl auf dem Bambus-Schneidebrett, dahinter frisches Gemüse"></div>
    <div class="features">
      <strong>Besonderheiten:</strong>
      - Saftrinne<br>
      - Giffmulden<br>
      - Amti-Rutsch-Füße
    </div>
    <div class="care">
      <svg width="40" height="40" viewBox="0 0 40 40" aria-hidden="true">
        <rect x="8" y="8" width="24" height="24" rx="2" fill="none" stroke="#b23a3a" stroke-width="2"/>
        <circle cx="20" cy="20" r="7" fill="none" stroke="#b23a3a" stroke-width="2"/>
        <line x1="4" y1="4" x2="36" y2="36" stroke="#b23a3a" stroke-width="2"/>
        <line x1="36" y1="4" x2="4" y2="36" stroke="#b23a3a" stroke-width="2"/>
      </svg>
      <span>NICHT SPÜLMASCHINENGEEIGNET</span>
    </div>
  </section>

  <section class="panel front">
    <h2 class="wordmark">KESTRILO</h2>
    <p class="label product-title">Bambus-Frühstücksbrettchen</p>
    <div class="product-shots">
      <div class="product-shot" role="img" aria-label="Foto: Brettchen-Set aufrecht im Ständer"></div>
      <div class="product-shot" role="img" aria-label="Foto: Brettchen-Set liegend gestapelt"></div>
      <div class="product-shot" role="img" aria-label="Foto: Brettchen-Set aufgefächert"></div>
    </div>
  </section>

  <section class="panel end">
    <div class="imprint">
      <p>Kestrilo GmbH<br>Musterstraße 12, 10115 Berlin<br>www.kestrilo.de</p>
    </div>
  </section>
</main>
</body>
</html>
```